amber lanterns

We are in need of a website for married spouses or wives that are looking for a one night stand or affair, trying to get out from their marriage routine. We want our website for married people only.

i have extended my deadline until the 29 of april. we are looking for at least 8 pages if possible, but we would only like to see the first page as an example for the next few pages. if we really like your design we weill hire you and thenĀ  we talk about the rest of the pages and the money. if you have any comments or questions, don't be afraid to ask.

• We want to be able to have a link open to a future website. it needs pop ups and ads. we would like it to say at the bottom of the page, bolded and highlighted that, " We are not responsible for any sexually transmitted diseases" and " We are not responsible for any marriage break-ups or any problems in consequence after the encounters." " It is the responsibility of the subscriber(member) to have enough information about the person before the encounter." We would like the website to be compatible to fundora. The subscribers must be able to web chat, upload photos, and upload videos but can decide who can see them or watch them.They can also have the choice to block certain members from their profile.

```html
<!DOCTYPE html>
<html lang="en">
<head>
<meta charset="utf-8">
<title>Amber Lanterns</title>
<link rel="stylesheet" href="https://fonts.googleapis.com/css2?family=Felipa&family=Cormorant+Garamond:ital,wght@0,400;1,400&family=Tinos:wght@400;700&family=Gochi+Hand&display=swap">
<style>
  :root {
    --red: #ff0000;
    --button-red: #ec1a1f;
    --page: #131112;
    --rule: #8a8a8a;
    --ink: #ffffff;
    --nav: #a3a3a3;
    --caption-bg: rgba(0, 0, 0, 0.62);
    --dot: #9c9a9c;
    --dot-active: #5c5a5c;
  }
  * { margin: 0; padding: 0; box-sizing: border-box; }
  html, body { width: 1200px; height: 900px; overflow: hidden; background: var(--page); }
  .page { position: relative; width: 1200px; height: 900px; background: var(--page); overflow: hidden; color: var(--ink); }

  .band { position: absolute; left: 0; width: 1200px; height: 20px; background: var(--red); }
  .band-top { top: 0; }
  .band-bottom { top: 880px; }

  .rule { position: absolute; background: var(--rule); }
  .rule-vertical { left: 870px; top: 28px; width: 1px; height: 794px; }
  .rule-header { left: 235px; top: 141px; width: 947px; height: 1px; }
  .rule-content { left: 235px; top: 573px; width: 947px; height: 1px; }

  .brand { position: absolute; left: 24px; top: 44px; font-family: "Felipa", cursive; font-size: 36px; line-height: 46px; letter-spacing: 2px; color: var(--ink); }
  .brand-line { display: block; }
  .brand-line-second { padding-left: 128px; }

  .phone { position: absolute; left: 1046px; top: 98px; font-family: "Cormorant Garamond", serif; font-size: 28px; letter-spacing: 4px; white-space: nowrap; width: 137px; overflow: hidden; }

  .hero { position: absolute; left: 5px; top: 146px; width: 858px; height: 420px;
    background: linear-gradient(120deg, #5a4a56 0%, #6e6070 30%, #8b3a4e 50%, #6a5666 70%, #4a3c46 100%); }
  .hero-caption { position: absolute; left: 0; top: 338px; width: 593px; height: 76px; background: var(--caption-bg);
    font-family: "Felipa", cursive; font-size: 27px; line-height: 33px; letter-spacing: 2px; padding: 3px 0 0 21px; }
  .hero-dots { position: absolute; left: 701px; top: 396px; display: flex; gap: 11px; }
  .hero-dot { width: 15px; height: 15px; border-radius: 50%; background: var(--dot); }
  .hero-dot-active { background: var(--dot-active); border: 1px solid #888; }

  .signup { position: absolute; left: 885px; top: 158px; width: 292px; }
  .signup-label { display: block; font-family: "Tinos", serif; font-size: 25px; color: var(--ink); margin-left: 1px; }
  .signup-field { display: block; width: 292px; height: 51px; background: #fff; border: 2px solid #9a9a9a; margin: 10px 0 25px; }
  .signup-field-last { margin-bottom: 23px; }
  .signup-button { position: absolute; left: 47px; top: 339px; width: 246px; height: 63px; background: var(--button-red); border: 2px solid #9a9a9a;
    font-family: "Tinos", serif; font-weight: 700; font-size: 34px; letter-spacing: 1px; color: var(--ink); text-shadow: 2px 2px 2px #3a0000;
    display: flex; align-items: center; justify-content: center; }

  .notice { position: absolute; left: 31px; top: 577px; font-family: "Cormorant Garamond", serif; font-style: italic; color: var(--ink); }
  .notice-title { font-size: 26px; line-height: 34px; }
  .notice-body { margin-left: 19px; font-size: 23px; line-height: 52.5px; width: 800px; }

  .side-photo { position: absolute; left: 898px; top: 580px; width: 265px; height: 239px; border-radius: 0 14px 0 0;
    background: linear-gradient(160deg, #e4e4e4 0%, #a8a8a8 45%, #5a5a5a 75%, #b8b8b8 100%); }

  .nav { position: absolute; left: 0; top: 822px; width: 1200px; height: 58px; background: var(--nav); display: flex; align-items: center; }
  .nav-item { font-family: "Gochi Hand", cursive; font-size: 25px; color: var(--ink); text-shadow: -1px -1px 0 #222, 1px -1px 0 #222, -1px 1px 0 #222, 1px 1px 0 #222;
    position: absolute; top: 14px; letter-spacing: 1px; }
  .nav-divider { position: absolute; top: 13px; width: 2px; height: 40px; background: #6f6f6f; }
</style>
</head>
<body>
<div class="page">
  <div class="band band-top"></div>

  <div class="brand">
    <span class="brand-line">Amber</span>
    <span class="brand-line brand-line-second">Lanterns</span>
  </div>
  <div class="phone">555-010-2</div>

  <div class="rule rule-vertical"></div>
  <div class="rule rule-header"></div>

  <section class="hero" role="img" aria-label="Photograph of a couple embracing on a sofa among cushions">
    <p class="hero-caption">Married spouses or wives that are<br>looking for a one night stand or affair</p>
    <div class="hero-dots">
      <span class="hero-dot hero-dot-active"></span>
      <span class="hero-dot"></span>
      <span class="hero-dot"></span>
      <span class="hero-dot"></span>
    </div>
  </section>

  <form class="signup">
    <label class="signup-label">Name:</label>
    <span class="signup-field"></span>
    <label class="signup-label">E-mail:</label>
    <span class="signup-field"></span>
    <label class="signup-label">Contact No:</label>
    <span class="signup-field signup-field-last"></span>
    <span class="signup-button">START NOW</span>
  </form>

  <div class="rule rule-content"></div>

  <section class="notice">
    <p class="notice-title">NOTE:</p>
    <p class="notice-body">We are not responsible for any sexually transmitted diseases" and "We are not responsible for any marriage break-ups or any problems in consequence after the encounters." "It is the responsibility of the subscriber(member) to have enough information about the person before the encounter."</p>
  </section>

  <div class="side-photo" role="img" aria-label="Black and white photograph of a couple embracing outdoors"></div>

  <nav class="nav">
    <span class="nav-item" style="left:46px">HOME</span>
    <span class="nav-divider" style="left:143px"></span>
    <span class="nav-item" style="left:162px">BLOGS</span>
    <span class="nav-divider" style="left:260px"></span>
    <span class="nav-item" style="left:278px">PICTURE</span>
    <span class="nav-divider" style="left:399px"></span>
    <span class="nav-item" style="left:418px">VIDEOS</span>
    <span class="nav-divider" style="left:528px"></span>
    <span class="nav-item" style="left:550px">SERVICES</span>
    <span class="nav-divider" style="left:685px"></span>
    <span class="nav-item" style="left:706px">ABOUT US</span>
    <span class="nav-divider" style="left:849px"></span>
    <span class="nav-item" style="left:868px">CONTACT US</span>
    <span class="nav-divider" style="left:1039px"></span>
    <span class="nav-item" style="left:1058px">PLACES</span>
  </nav>

  <div class="band band-bottom"></div>
</div>
</body>
</html>
```